WORDPRESS WEB DESIGN PROJECT-DESIGN & DEVELOP

OUR BUSINESS
Bright Harbour Consulting provides effective project controls and management solutions for construction projects in Australia and Overseas. We provide services to both large multinational companies and smaller privately owned businesses. Our knowledge and expertise assist clients to effectively plan and manage their construction projects or project portfolios. Our focus is to provide your business with the tools, solutions and strategies necessary to deliver projects on time and within budget.

WHY WE ARE RE-BRANDING OUR WEBSITE
Our existing website design is not effective at promoting our business. We require a fresh, new, innovative approach to effectively market our business brand. Our new website will have the same look and feed as our newly developed business brochure.

DESIGN
Our new website will have the same look and feed as our business brochure. This website will be developed in Word press; a customized theme is required. The graphic design and images will enhance the written content; any graphics need to be developed in Photoshop as this is the software we use. A horizontal navigation menu will be implemented but must blend into the design and not be contained in a colour band. The webpage itself needs to span the entire viewable screen and must not look like an A4 piece of paper on a colored background. Additional design comments have been attached to this project as " website contents" word doc.

WEDSITES I LIKE THE LOOK OF
www.example-tarvion.com (very professional, similar color scheme)
www.example-quellory.com ( Good design, background made the website pop)
www.example-brimwoodfloorcare.com.au (clean,tidy,sharp images)
www.example-velantis.com ( the look was simple but effective)
http://www.example-norvik.com

STYLE
We require a stylish, clean and easy to navigate website, with fresh, exciting and engaging imagery. Our website design needs to be modern, clean and sleek.

WRITTEN CONTENT
New written content for each page is provided with this project, there is 50% less content in this project than the original website.

QUALITY
High resolution images and photos will be used to promote an overall quality, professional look and feel.

FUNCTIONALITY
The design needs to be easily updated and editable. The person updating the webpage content and images does not know coding, so the theme will need to be able to interact with plugins. All design components need to be optimized for indexing on major search engines e.g. Firefox, internet explorer, Google and safari.

ICONS
I will require icon links to Email, Facebook and LinkedIn, but not for twitter, Gmail or live feeds.

MENU
1.Home
2.Services
3.Benefits
4.Management
5.Planning
6.Optimization
7.Industry
8.Software
9.Contact us
10.Recruitment

TARGET AUDIENCE
Corporate Clients in all industry’s sectors
Supporting clients in
★OIL & Gas
★Iron Ore
★Coal
★New Industries
★Building and Construction
★Rail
★Civil
★Manufacturing
★Petrochemical
★Telecommunications

THE WINNER WILL PROVIDE
1. Wordpress theme with design.
2. List of plugins needed to meet requirements or design.
3. All images used in design.
4. Any custom php, javascript, or css files needed for the design.
5. List of core wordpress files customized as part of the design.
6. Any source files for custom images or design work (psd)

ATTACHMENTS
The following items will be attached to this project
1. Business logo
2. Icon images
3. Business Brochure PDF
4. Business brochure cover page psd file
5. Content required in each webpage

DESIGN AND DEVELOP
This project is to design and develop a word press website. In respect that the chosen designer may not be able to provide the development, 2 places of $400 each have been offered (1st for the design aspect, and 2nd for the development). The winning designer will receive $800 if both design and development have been achieved.

PROJECT CHANGES

The projects budget has increased from $600 to $800

Completion date has extended by 7 day.

Requirements
Should not have
• This design must have not appear out-dated or cluttered
Please do not provide any designs that look like our old website.

```html
<!DOCTYPE html>
<html lang="en">
<head>
<meta charset="utf-8">
<title>Bright Harbour Consulting</title>
<link href="https://fonts.googleapis.com/css2?family=Open+Sans:wght@400;600;700&display=swap" rel="stylesheet">
<style>
:root{
  --red:#d71920;
  --ink:#222;
  --text:#555;
  --muted:#888;
  --band:#f2f2f2;
  --dark:#2e2e2e;
  --darker:#262626;
  --line:#e4e4e4;
}
*{box-sizing:border-box;margin:0;padding:0}
html,body{width:783px;height:1200px;overflow:hidden;background:#fff}
body{font-family:"Open Sans",sans-serif;color:var(--ink);position:relative}
.abs{position:absolute}
/* header */
.site-header{position:absolute;left:0;top:0;width:783px;height:72px;background:linear-gradient(#fff,#f0f0f0);border-bottom:1px solid var(--line)}
.brand{left:73px;top:22px;display:flex;align-items:center;gap:8px}
.brand-mark{width:26px;height:26px;border-radius:50%;background:var(--red)}
.brand-name{font-size:17px;font-weight:700;color:var(--ink)}
.social{left:483px;top:25px;display:flex;gap:5px}
.social span{width:21px;height:21px;border-radius:50%;border:1px solid #ccc;background:#fff;display:block}
.call-btn{left:618px;top:23px;width:90px;height:26px;background:#1e1e1e;color:#fff;border-radius:4px 13px 13px 4px;font-size:12px;text-align:center;line-height:26px}
/* nav */
.main-nav{left:0;top:73px;width:783px;height:35px;display:flex;padding-left:70px;font-size:8.6px;color:#333}
.main-nav a{color:inherit;text-decoration:none;padding:0 13px;line-height:35px}
.main-nav a.active{border-top:1px solid var(--red)}
/* hero */
.hero{left:0;top:108px;width:783px;height:240px;background:linear-gradient(90deg,#8a5a3a 0%,#b97a52 25%,#9aa3ad 45%,#c9c3bb 70%,#d8d3cc 100%)}
.hero-copy{left:435px;top:142px;width:320px}
.hero-copy h1{font-size:27px;font-weight:400;line-height:27px;color:#111}
.hero-copy p{font-size:10px;line-height:12.5px;color:#fff;margin-top:12px;width:250px}
.btn-red{display:inline-block;background:var(--red);color:#fff;font-size:8px;border-radius:12px;padding:0 15px;height:25px;line-height:25px;margin-top:9px}
/* intro */
.intro{left:0;top:348px;width:783px;height:118px;background:var(--band);text-align:center;border-bottom:1px solid #e2e2e2}
.intro p{font-size:12px;line-height:17px;color:#333;padding:22px 70px 0;font-weight:400}
.intro strong{color:var(--red);font-weight:600}
.intro-actions{display:flex;justify-content:center;gap:5px;margin-top:10px}
.btn-dark{background:#1c1c1c;color:#fff;font-size:9px;font-weight:600;height:25px;line-height:25px;padding:0 10px;border-radius:2px}
/* industries */
.industry{width:185px}
.industry-head{display:flex;align-items:center;gap:8px;border-bottom:1px solid var(--line);padding-bottom:6px;position:relative}
.industry-head::after{content:"";position:absolute;left:34px;bottom:-1px;width:42px;height:1px;background:var(--red)}
.icon-circle{width:27px;height:27px;border-radius:50%;background:#2a2a2a;flex:none;display:flex;align-items:center;justify-content:center}
.industry-head h3{font-size:10px;font-weight:400}
.industry p{font-size:7.4px;line-height:9.7px;color:var(--muted);padding:8px 0 0 36px}
.view-all{left:629px;top:686px;font-size:8px;color:var(--red);text-decoration:underline;font-style:italic}
.pager{left:669px;top:686px;display:flex;gap:2px}
.pager span{width:12px;height:12px;background:#eee;display:block}
/* services */
.services{left:0;top:712px;width:783px;height:232px;background:var(--band);border-top:1px solid #e6e6e6}
.card{width:196px}
.card-photo{height:98px;width:196px}
.card h3{font-size:10px;font-weight:400;margin:7px 0 0 1px}
.card p{font-size:7.4px;line-height:9.3px;color:var(--muted);margin:9px 2px 0}
.btn-pill{display:inline-block;background:#1c1c1c;color:#fff;font-size:6.5px;height:19px;line-height:19px;padding:0 11px;border-radius:0 10px 10px 10px;margin:10px 0 0 2px}
/* partners */
.partners{left:80px;top:968px;width:620px;display:flex;justify-content:space-between;align-items:center;height:50px}
.partner{font-size:11px;font-weight:700;color:#555;display:flex;align-items:center;gap:5px}
.partner i{width:14px;height:14px;background:#6a6a6a;border-radius:50%;display:block}
/* footer */
.site-footer{left:0;top:1043px;width:783px;height:157px;background:var(--dark);border-top:3px solid #3a3a3a}
.foot-col h4{font-size:10px;font-weight:600;color:#fff;margin-bottom:8px}
.foot-col li{list-style:none;font-size:7.6px;line-height:11.7px;color:#999}
.newsletter{width:166px;height:22px;background:#fff;border:1px solid #ccc;font-size:6.5px;font-style:italic;color:#aaa;padding-left:9px;line-height:21px}
.foot-social{display:flex;gap:6px;margin-top:10px}
.foot-social span{width:15px;height:15px;border-radius:3px;display:block;background:#4a7fc0}
.foot-social span:nth-child(4){background:var(--red)}
.foot-base{left:80px;top:1164px;width:610px;border-top:1px solid #444;text-align:center;font-size:7.6px;color:#ddd;padding-top:10px}
</style>
</head>
<body>

<header class="site-header">
  <div class="abs brand"><span class="brand-mark"></span><span class="brand-name">Bright Harbour Consulting</span></div>
  <div class="abs social"><span></span><span></span><span></span><span></span><span></span></div>
  <div class="abs call-btn">Call Today</div>
</header>

<nav class="abs main-nav">
  <a class="active">Home</a><a>Services</a><a>Benefits</a><a>Management</a><a>Planning</a><a>Optimization</a><a>Industry</a><a>Software</a><a>Contact Us</a><a>Recruitment</a>
</nav>

<section class="abs hero" role="img" aria-label="Industrial refinery with chimneys and smoke under an overcast sky"></section>
<div class="abs hero-copy">
  <h1>Projects Controls<br>Management Systems</h1>
  <p>We can design and implemented project controls management system to provide the structural frame work required to accurately monitor</p>
  <span class="btn-red">Read More</span>
</div>

<section class="abs intro">
  <p><strong>Bright Harbour Consulting</strong>&nbsp; Provides effective project controls and management slоutions for construction projects in Australia and Overseas. We provide services to both large multination companies and smaller privately owned businesses.</p>
  <div class="intro-actions"><span class="btn-dark">SEE FEATURES</span><span class="btn-dark" style="padding:0 19px">CONTACT US</span></div>
</section>

<section class="industries">
  <div class="abs industry" style="left:77px;top:498px"><div class="industry-head"><span class="icon-circle"><svg width="13" height="11"><rect x="1" y="5" width="2" height="6" fill="#fff"/><rect x="5" y="2" width="2" height="9" fill="#fff"/><rect x="9" y="0" width="2" height="11" fill="#fff"/></svg></span><h3>Oil &amp; Gas</h3></div><p>Lorem Ipsum is simply dummy text of the printing and typesetting industry. Lorem Ipsum has been the industry's standard dummy text ever since the</p></div>
  <div class="abs industry" style="left:300px;top:498px"><div class="industry-head"><span class="icon-circle"><svg width="11" height="13"><rect x="1" y="1" width="9" height="11" fill="none" stroke="#fff" stroke-width="1.5"/></svg></span><h3>Petrochemical</h3></div><p>Lorem Ipsum is simply dummy text of the printing and typesetting industry. Lorem Ipsum has been the industry's standard dummy text ever since the</p></div>
  <div class="abs industry" style="left:524px;top:498px"><div class="industry-head"><span class="icon-circle"><svg width="11" height="12"><rect x="1" y="1" width="9" height="10" fill="var(--red)"/><rect x="3" y="3" width="2" height="2" fill="#fff"/><rect x="6" y="3" width="2" height="2" fill="#fff"/><rect x="3" y="7" width="2" height="2" fill="#fff"/><rect x="6" y="7" width="2" height="2" fill="#fff"/></svg></span><h3>Building &amp; Construction</h3></div><p>Lorem Ipsum is simply dummy text of the printing and typesetting industry. Lorem Ipsum has been the industry's standard dummy text ever since the</p></div>
  <div class="abs industry" style="left:77px;top:595px"><div class="industry-head"><span class="icon-circle"><svg width="13" height="12"><path d="M1 5 Q6.5 0 12 5 L10 6 L8 4 L5 4 L3 6Z" fill="#fff"/><rect x="3" y="7" width="7" height="4" fill="#fff"/></svg></span><h3>Telecommunications</h3></div><p>Lorem Ipsum is simply dummy text of the printing and typesetting industry. Lorem Ipsum has been the industry's standard dummy text ever since the</p></div>
  <div class="abs industry" style="left:300px;top:595px"><div class="industry-head"><span class="icon-circle"><svg width="13" height="12"><path d="M1 11V2M1 11H12M3 11V5M6 11V6M9 11V4" stroke="#fff" stroke-width="1.4"/></svg></span><h3>Manufacturing</h3></div><p>Lorem Ipsum is simply dummy text of the printing and typesetting industry. Lorem Ipsum has been the industry's standard dummy text ever since the</p></div>
  <div class="abs industry" style="left:524px;top:595px"><div class="industry-head"><span class="icon-circle"><svg width="13" height="12"><path d="M1 11V4L5 6V4L9 6V1H12V11Z" fill="#fff"/><rect x="9" y="0" width="3" height="2" fill="var(--red)"/></svg></span><h3>New Industries</h3></div><p>Lorem Ipsum is simply dummy text of the printing and typesetting industry. Lorem Ipsum has been the industry's standard dummy text ever since the</p></div>
  <span class="abs view-all">View all</span>
  <div class="abs pager"><span></span><span></span></div>
</section>

<section class="abs services"></section>
<div class="abs card" style="left:84px;top:737px"><div class="card-photo" role="img" aria-label="Oil pump jack in a grassy field under blue sky" style="background:linear-gradient(#3d6fb0 0%,#7ba3d4 55%,#8a8a3a 70%,#6a6a2c 100%)"></div><h3>Identify Project risks</h3><p>Lorem Ipsum is simply dummy text of the printing and typesetting industry. Lorem Ipsum has been the industry's standard dummy text ever since the 1500s,</p><span class="btn-pill">Read More</span></div>
<div class="abs card" style="left:293px;top:737px"><div class="card-photo" role="img" aria-label="Pipelines leading to a refinery" style="background:linear-gradient(#c8ccd0 0%,#9aa29a 45%,#7a7e78 70%,#a8aaa6 100%)"></div><h3>Plan &amp; Control Budgets</h3><p>Lorem Ipsum is simply dummy text of the printing and typesetting industry. Lorem Ipsum has been the industry's standard dummy text ever since the 1500s,</p><span class="btn-pill">Read More</span></div>
<div class="abs card" style="left:501px;top:737px"><div class="card-photo" role="img" aria-label="Blue-lit industrial pipework reflected in water" style="background:linear-gradient(135deg,#0b2a55 0%,#2d6fb8 45%,#9cc6ec 65%,#103a70 100%)"></div><h3>Stream line processes</h3><p>Lorem Ipsum is simply dummy text of the printing and typesetting industry. Lorem Ipsum has been the industry's standard dummy text ever since the 1500s,</p><span class="btn-pill">Read More</span></div>

<div class="abs partners">
  <span class="partner"><i></i>Southwind Gas</span>
  <span class="partner">Corvane Energy</span>
  <span class="partner">Redvale Mining</span>
  <span class="partner">Tallow Coal</span>
  <span class="partner">Ironmere Group</span>
  <span class="partner"><i></i>Westreach Ore</span>
</div>

<footer class="abs site-footer">
  <div class="abs foot-col" style="left:80px;top:22px"><h4>Links</h4><ul><li>Home</li><li>About Us</li><li>Benefits</li><li>Management</li></ul></div>
  <div class="abs foot-col" style="left:197px;top:22px"><h4>About Us</h4><ul><li>Oil &amp; Gas</li><li>Telecommunicatios</li><li>New Industries</li></ul></div>
  <div class="abs foot-col" style="left:320px;top:22px"><h4>Connect with us</h4><ul><li>hello@brightharbourconsulting.example</li><li>+61 0400 000 000</li></ul></div>
  <div class="abs foot-col" style="left:539px;top:22px"><h4>Sign up for newsletter</h4><div class="newsletter">Enter Your Email Address</div><div class="foot-social"><span></span><span></span><span></span><span></span></div></div>
</footer>
<div class="abs foot-base">2013, Bright Harbour Consulting. Privacy Policy &nbsp;| &nbsp;Terms of Service &nbsp;| &nbsp;Help &nbsp;| &nbsp;Contact</div>

</body>
</html>
```